We are a building company that build new homes and units we are looking for something fresh and looks good my company name is
Larkmoor Building Group Pty Ltd

Industry/Entity Type

Building

Contact Information for Business Card

Name Marco Delacruz-Fenn
Tittle: Director
Address 14 Quarrel St. Thornbury Vic 3071
Ph: 03 9612 4087
Mobile : 0400 562 938

www.larkmoorbuildinggroup.com.au
Email: sales@larkmoorbuildinggroup.com.au

```html
<!DOCTYPE html>
<html lang="en">
<head>
<meta charset="utf-8">
<title>Larkmoor Building Group – Business Card</title>
<link rel="stylesheet" href="https://fonts.googleapis.com/css2?family=Montserrat:ital,wght@0,300;0,400;0,500;0,700;1,400&display=swap">
<style>
  :root {
    --navy: #0c2d80;
    --blue: #5585e9;
    --band: #b8d4ea;
    --white: #ffffff;
    --sky-top: #e2edf9;
    --sky-bottom: #c9cfd6;
  }
  * { margin: 0; padding: 0; box-sizing: border-box; }
  html, body { width: 1200px; height: 1000px; overflow: hidden; background: var(--white); }
  body { position: relative; font-family: "Montserrat", sans-serif; }

  .card { position: absolute; top: 114px; width: 428px; height: 660px; overflow: hidden; }
  .card--front { left: 136px; background: var(--navy); }
  .card--back { left: 629px; background: var(--blue); }

  /* Front */
  .front-photo {
    position: absolute; left: 0; top: 0; width: 428px; height: 360px;
    background: linear-gradient(180deg, var(--sky-top) 0%, #d9dde2 45%, var(--sky-bottom) 100%);
  }
  .front-angles { position: absolute; left: 0; top: 0; width: 428px; height: 660px; }
  .front-wordmark {
    position: absolute; right: 40px; top: 78px; width: 240px;
    text-align: right; color: var(--navy); font-weight: 700;
    font-size: 30px; line-height: 1.12; text-transform: uppercase;
  }
  .person { position: absolute; left: 167px; top: 378px; }
  .person__name { color: var(--blue); font-size: 21px; font-weight: 400; }
  .person__title { color: var(--white); font-size: 11px; font-weight: 500; margin-top: 5px; margin-left: 2px; }

  .contact { position: absolute; left: 89px; top: 484px; color: var(--white); font-size: 18px; }
  .contact__row { display: flex; line-height: 22px; margin-bottom: 5px; }
  .contact__label { color: var(--blue); font-weight: 500; width: 21px; }
  .contact__row--email { font-size: 15px; }
  .contact__web { font-size: 17px; margin-top: 4px; }

  /* Back */
  .back-wordmark {
    position: absolute; left: 0; top: 48px; width: 428px;
    text-align: center; color: var(--navy); font-weight: 700;
    font-size: 28px; line-height: 1.15; text-transform: uppercase;
  }
  .tagline-band {
    position: absolute; left: 0; top: 204px; width: 428px; height: 40px;
    background: var(--band); color: var(--navy);
    font-size: 18px; font-weight: 500; text-align: center; line-height: 40px;
  }
  .statement {
    position: absolute; left: 20px; top: 266px; width: 388px;
    color: var(--white); font-style: italic; font-size: 17px; line-height: 22px; text-align: center;
  }
  .back-photo {
    position: absolute; left: 0; top: 404px; width: 428px; height: 256px;
    background: linear-gradient(160deg, #a5c6ee 0%, #cfe0f2 35%, #e8e2d8 55%, #c8784a 78%, #4d6b3a 100%);
  }
</style>
</head>
<body>

<section class="card card--front">
  <div class="front-photo" role="img" aria-label="Photo of a modern two-storey home with a white balcony under a pale sky"></div>
  <svg class="front-angles" viewBox="0 0 428 660" aria-hidden="true">
    <polygon points="0,353 428,285 428,320 0,353" fill="#5585e9"/>
    <polygon points="0,353 428,319 428,660 0,660" fill="#0c2d80"/>
  </svg>
  <div class="front-wordmark">Larkmoor Building Group Pty Ltd</div>

  <div class="person">
    <div class="person__name">Marco Delacruz-Fenn</div>
    <div class="person__title">DIRECTOR</div>
  </div>

  <div class="contact">
    <div class="contact__row"><span class="contact__label">A</span><span>14 Quarrel Street<br>Thornbury VIC 3071</span></div>
    <div class="contact__row"><span class="contact__label">P</span><span>03 9612 4087</span></div>
    <div class="contact__row"><span class="contact__label">M</span><span>0400 562 938</span></div>
    <div class="contact__row contact__row--email"><span class="contact__label" style="font-size:18px">E</span><span>sales@larkmoorbuildinggroup.com.au</span></div>
    <div class="contact__web">www.larkmoorbuildinggroup.com.au</div>
  </div>
</section>

<section class="card card--back">
  <div class="back-wordmark">Larkmoor<br>Building Group<br>Pty Ltd</div>
  <div class="tagline-band">Quality, excellence and innovation.</div>
  <p class="statement">Our unwavering commitment to quality and excellence in home design has helped us become Australia’s market leader in new home design and construction.</p>
  <div class="back-photo" role="img" aria-label="Photo of a modern townhouse row with timber screens, balconies and trees against a blue sky"></div>
</section>

</body>
</html>
```